QM Fenwold Detailing, Inc.

I'm looking for business card design for an existing company with an existing logo/website. www.qmfenwold-detailing.com. VETERAN OWNED logo must be present.

Target Market(s)

Structural and architectural steel fabricators

Industry/Entity Type

Structural and architectural steel detailing and engineering

Contact Information for Business Card

logo, business name, address, phone, website, email, employee info

Font styles to use
Serif

Colors
00AB8E
00BBA5
67D7C9
C6EFE9
E9F9F6

Requirements
Must have
• company logo, website, VETERAN OWNED LOGO
Should not have
• Don't make it too busy. Less is more

```html
<!DOCTYPE html>
<html lang="en">
<head>
<meta charset="utf-8">
<title>QM Fenwold Detailing — Business Card</title>
<link href="https://fonts.googleapis.com/css2?family=PT+Serif:wght@400;700&display=swap" rel="stylesheet">
<style>
  :root {
    --brand: #00ab8e;
    --brand-light: #00bba5;
    --ink: #555555;
    --paper: #ffffff;
    --backdrop: #6b6b6b;
  }
  * { margin: 0; padding: 0; box-sizing: border-box; }
  html, body { width: 1200px; height: 1200px; overflow: hidden; }
  body {
    background: var(--backdrop);
    font-family: "PT Serif", Georgia, serif;
    position: relative;
  }
  .card {
    position: absolute;
    left: 250px;
    width: 700px;
    height: 400px;
    background: var(--paper);
    overflow: hidden;
  }
  .card--front { top: 159px; }
  .card--back { top: 623px; }

  .veteran-badge {
    position: absolute;
    left: 70px; top: 73px;
    width: 104px; height: 104px;
    border-radius: 50%;
    background: var(--brand);
  }
  .brand-name {
    position: absolute;
    left: 69px; top: 268px;
    color: var(--brand);
    font-weight: 700;
    font-size: 24px;
    line-height: 28px;
  }
  .accent-band { position: absolute; left: 0; top: 0; }

  .contact {
    position: absolute;
    right: 80px; top: 86px;
    text-align: right;
    color: var(--ink);
  }
  .contact__name {
    color: var(--brand);
    font-size: 26px;
    font-weight: 400;
    line-height: 1;
  }
  .contact__title {
    font-size: 13px;
    margin-top: 5px;
    letter-spacing: 0.3px;
  }
  .contact__row {
    display: flex;
    justify-content: flex-end;
    align-items: center;
    gap: 13px;
    font-size: 17px;
    line-height: 24px;
  }
  .contact__row--phone { margin-top: 12px; }
  .contact__row--email { margin-top: 7px; }
  .contact__company {
    color: var(--brand);
    font-weight: 700;
    font-size: 18px;
    line-height: 24px;
    margin-top: 7px;
  }
  .contact__row--address { margin-top: 5px; }
  .contact__city { font-size: 17px; line-height: 24px; margin-right: 37px; margin-top: 2px; }
  .icon {
    width: 24px; height: 24px;
    background: var(--brand);
    display: flex; align-items: center; justify-content: center;
    flex: none;
  }

  .back-wedges { position: absolute; left: 0; top: 0; }
  .back-brand {
    position: absolute;
    left: 0; right: 0; top: 165px;
    text-align: center;
    color: var(--brand);
    font-weight: 700;
    font-size: 40px;
    line-height: 1;
  }
  .back-website {
    position: absolute;
    left: 0; right: 0; top: 288px;
    text-align: center;
    color: var(--brand);
    font-weight: 700;
    font-size: 18px;
    line-height: 24px;
  }
</style>
</head>
<body>

<section class="card card--front">
  <div class="veteran-badge" role="img" aria-label="Veteran owned small business badge"></div>

  <div class="contact">
    <h1 class="contact__name">DANIEL MARSH</h1>
    <p class="contact__title">MANAGER</p>
    <p class="contact__row contact__row--phone">
      <span>555.014.2207</span>
      <span class="icon">
        <svg width="14" height="14" viewBox="0 0 24 24"><path fill="#fff" d="M6.6 10.8c1.4 2.8 3.8 5.1 6.6 6.6l2.2-2.2c.3-.3.7-.4 1-.2 1.1.4 2.3.6 3.6.6.6 0 1 .4 1 1V20c0 .6-.4 1-1 1C10.6 21 3 13.4 3 4c0-.6.4-1 1-1h3.5c.6 0 1 .4 1 1 0 1.3.2 2.5.6 3.6.1.3 0 .7-.2 1z"/></svg>
      </span>
    </p>
    <p class="contact__row contact__row--email">
      <span>sales@qmfenwold-detailing.com</span>
      <span class="icon">
        <svg width="14" height="10" viewBox="0 0 14 10"><rect x="0" y="0" width="14" height="10" fill="#fff"/><path d="M0.5 0.8 7 5.8 13.5 0.8" fill="none" stroke="#00ab8e" stroke-width="1.4"/></svg>
      </span>
    </p>
    <p class="contact__company">QM Fenwold Detailing</p>
    <p class="contact__row contact__row--address">
      <span>4180 Harbor View Blvd., ste 310</span>
      <span class="icon">
        <svg width="12" height="16" viewBox="0 0 12 16"><path fill="#fff" d="M6 0C2.7 0 0 2.6 0 5.9 0 10.2 6 16 6 16s6-5.8 6-10.1C12 2.6 9.3 0 6 0zm0 8.2a2.3 2.3 0 1 1 0-4.6 2.3 2.3 0 0 1 0 4.6z"/></svg>
      </span>
    </p>
    <p class="contact__city">Clearwater, FL 33755</p>
  </div>

  <p class="brand-name">QM Fenwold<br>Detailing</p>

  <svg class="accent-band" width="700" height="400" viewBox="0 0 700 400" aria-hidden="true">
    <polygon points="208,305 700,305 700,330 223,330" fill="var(--brand)"/>
  </svg>
</section>

<section class="card card--back">
  <svg class="back-wedges" width="700" height="400" viewBox="0 0 700 400" aria-hidden="true">
    <polygon points="0,86 52,199 0,313" fill="var(--brand)"/>
    <polygon points="700,86 648,199 700,313" fill="var(--brand)"/>
  </svg>
  <p class="back-brand">QM Fenwold Detailing</p>
  <p class="back-website">www.qmfenwold-detailing.com</p>
</section>

</body>
</html>
```